Gentle Kundalini Yoga with Gong Relaxation

I teach a gentle Kundalini Yoga class with Gong relaxation every Thursday morning from 8:30-10am at the Ashford Meadows Unity Chapel 17 Garber Lane Pellam Crest. This class is unique in that I play the gong for an extended relaxation. Gongs are generally only found in established Yoga centers not in a small neighborhood yoga class. I am trying to grow this class from a current class size of 5 students. I would like to double the class size.
Updates
Project Deadline Extended
Reason: We had a blizzard on January 27 and 28 in the Boston area and I was too busy removing snow to tend to the postcard design-Thank you-Dora Fitchley
Industry/Entity Type
Church

```html
<!DOCTYPE html>
<html lang="en">
<head>
<meta charset="utf-8">
<title>Deep Relaxation – Kundalini Yoga with Gong</title>
<link rel="stylesheet" href="https://fonts.googleapis.com/css2?family=Tinos&family=Open+Sans:wght@400&display=swap">
<style>
  :root {
    --lavender: #d9d3e8;
    --lavender-deep: #cfc7e2;
    --mist: #e4f4f4;
    --ink: #2a2d45;
    --white: #ffffff;
    --gong-light: #e6e6e4;
    --gong-edge: #8a8a88;
    --frame: #9a9a9a;
  }
  html, body {
    margin: 0;
    padding: 0;
    overflow: hidden;
    background: #ffffff;
  }
  .postcard {
    position: relative;
    width: 1200px;
    height: 935px;
    box-sizing: border-box;
    border: 2px solid var(--frame);
    overflow: hidden;
    background:
      radial-gradient(ellipse 420px 40px at 330px 45px, var(--mist), transparent 70%),
      radial-gradient(ellipse 180px 40px at 1050px 250px, var(--mist), transparent 70%),
      radial-gradient(ellipse 300px 45px at 830px 545px, var(--mist), transparent 70%),
      radial-gradient(ellipse 260px 40px at 200px 805px, var(--mist), transparent 70%),
      linear-gradient(180deg, var(--lavender), var(--lavender-deep));
    font-family: "Tinos", "Times New Roman", serif;
    color: var(--ink);
  }
  .gong-art {
    position: absolute;
    left: 78px;
    top: 62px;
    width: 540px;
    height: 540px;
    border-radius: 50%;
    background: radial-gradient(circle at 50% 50%, var(--gong-light) 60%, #c9c9c7 92%, var(--gong-edge) 100%);
  }
  .headline {
    position: absolute;
    right: 64px;
    top: 282px;
    margin: 0;
    font-weight: 400;
    font-size: 96px;
    line-height: 98px;
    text-align: right;
    color: var(--white);
  }
  .day {
    position: absolute;
    right: 762px;
    top: 636px;
    text-align: right;
    font-size: 34px;
    line-height: 36px;
  }
  .day span { display: block; }
  .class-name {
    position: absolute;
    left: 446px;
    top: 628px;
    margin: 0;
    font-weight: 400;
    font-size: 88px;
    line-height: 96px;
    letter-spacing: 1px;
  }
  .class-word {
    position: absolute;
    left: 1032px;
    top: 738px;
    font-size: 36px;
  }
  .venue {
    position: absolute;
    right: 198px;
    top: 732px;
    margin: 0;
    text-align: right;
    font-family: "Open Sans", Arial, sans-serif;
    font-size: 21px;
    line-height: 32px;
  }
  .extra {
    position: absolute;
    left: 460px;
    top: 800px;
    font-size: 50px;
  }
</style>
</head>
<body>
  <main class="postcard">
    <div class="gong-art" role="img" aria-label="Illustration of a gong with a brush-stroke circle and a striking mallet"></div>

    <h1 class="headline">Deep<br>Relaxation</h1>

    <div class="day"><span>Every</span><span>Thursday moning</span></div>
    <h2 class="class-name">Kundalini Yoga</h2>
    <div class="class-word">class</div>

    <p class="venue">from 8:30-10am at the Ashford Meadows Unity Chapel<br>17 Garber Lane Pellam Crest.</p>

    <div class="extra">with Gong relaxation</div>
  </main>
</body>
</html>
```